Lumen Botanicals Label Project- Updates made to project!

Project Scope: Branding opportunity for internet based skin care line. Design coordinating label for 4 different products. Each design shall be editable in Adobe Illustrator as a template including all fonts, symbols, and guides. Submit a design for all 4 products (preferably together as it would look on a retail shelf), business card, and logo.
Cleanser: STEP 1 Label Size: 5 x 4.5 inches (w x h) CALM CLEANSER
Toner: STEP 2 Label Size: 5 x 4.5 inches (w x h) TRANQUIL TONER- A piece of each crystal sits at the bottom of each solution. It coordinates with the "Quiet Heart" of our logo.
Serum STEP 3 Label Size: Label Size: 4.25 x 2.25 ANTI-AGING SERUM
Moisturizer: STEP 4 Label Size: Label Size: 1”x7.25” MOISTURIZER
Each label needs to include:
Front:
Attractive larger sized STEP #
Logo
Product name and short description
Decorative design Symbol(s)
Back:
Area on back to say short description
Directions for use
Larger area for ingredients
Website: www.lumenbotanicals-example.com
Address of distribution
Barcode

Lumen Skin Care, an esthetician created line provides organic and natural based products for all skin types. With an emphasis on anti-aging, this simple 4- step system can be used by many including pregnant and oncology consumers. The unique thing about our line is that the toners and serums contain crystals such as amethyst and rose quarts to promote Quiet Heart as well as outer beauty. Each product is handmade with natural, quality ingredients and are 70-90% Organic.
Target Market: Women ages 30-45 years old. This demographic is on the go, and wants a simple-easy to read label, & a skin care system that addresses her concerns. Just as this consumer is mindful of her fitness and what she puts in her body, she tends to purchase environmentally friendly, and natural products. Health and wellness trends reflect this, as organic beauty products are expected to grow 74% from 2013 to 2018. She enjoys meditation and yoga, and she is curious about eastern medicine holistic healing trends.

Company Name: Lumen Skin Care
Tagline: Quiet Heart- Bright Face
Package Feel: Simple, elegant easy to read step on each product. STEP 1: AM/PM. Attractive numbering. A symbol that reflects the brand. Not necessarily a Lumen or Crystal because the name speaks for itself. Beautiful, soft, eye catching design that draws the consumer to pick it up. Clear or white label welcomed. Some color palettes provided.
Descriptive words the packaging should represent: Yoga, Zen, mystic, eye catching, healing energy, natural, quality ingredients, sophisticated, beautiful, serenity, easy to read- bold-attractive numbering on front.
Inspiration Brands: VARLA Organics- Beautiful watercolor packaging that resonates a "feeling"

Attached are pictures of the packaging, inspirational pictures, skin care lines that are attractive, ect.

Packaging SPECS:

Cleanser:
Color Clear
Size 4 oz
Material PET
Case Pack
Neck Finish 24-410
Diameter 1.58 in / 4.013 cm
Height 6 in / 15.240 cm
Label Dimensions 5x4.5
Print Dimensions 5x4.5
Print Dimensions in (diameter)

TONER BOTTLE: Same as above

SERUM BOTTLE:
Color Clear
Size 2 oz
Material PET
Neck Finish 20-410
Diameter 1.358 in / 3.449 cm
Height 3.274 in / 8.316 cm

Moisturizer:
2.3 oz
Height:53 mm
Diameter: 60 mm
Neck: 58/400

Target Market(s)

Women ages 30-45 years old. This demographic is on the go, and wants a simple-easy to read label, & a skin care system that addresses her concerns. Just as this consumer is mindful of her fitness and what she puts in her body, she tends to purchase environmentally friendly, and natural products. Health and wellness trends reflect this, as organic beauty products are expected to grow 74% from 2013 to 2018. She enjoys meditation and yoga, and she is curious about eastern medicine holistic healing trends.

Industry/Entity Type

Skin Care Product

Contact Information for Business Card

Details given upon completion.

Logo Text

Lumen Botanicals Quiet Heart- Bright Face

Requirements
Must have
• A large step number on the front. Coordinating symbols and colors. Must have a professional retail look and be easy to read.
Nice to have
• Clean, simple, eye catching packaging. Watercolor designs. Designs that inspire "feelings" www.varlaorganics-example.com

```html
<!DOCTYPE html>
<html lang="en">
<head>
<meta charset="utf-8">
<title>Lumen Skin Care – Label System</title>
<link rel="stylesheet" href="https://fonts.googleapis.com/css2?family=Arimo:wght@400;700&family=Bodoni+Moda:wght@400&display=swap">
<style>
  :root {
    --blush: #f4b3af;
    --blush-deep: #efa8a4;
    --blush-soft: #f9d3d0;
    --silver: #d9d4d6;
    --silver-light: #ece8e9;
    --ink: #000000;
    --paper: #ffffff;
    --text: #111111;
    --label-text: #f7c9c5;
  }
  * { box-sizing: border-box; margin: 0; padding: 0; }
  html, body { width: 1200px; height: 1000px; overflow: hidden; background: var(--paper); }
  .canvas { position: relative; width: 1200px; height: 1000px; font-family: "Arimo", Arial, sans-serif; color: var(--text); }

  /* Brand banner */
  .brand-banner { position: absolute; left: 637px; top: 68px; width: 536px; height: 230px; overflow: hidden; }
  .banner-pattern {
    position: absolute; inset: 0;
    background:
      radial-gradient(ellipse 30% 45% at 12% 40%, rgba(236,232,233,0.55), transparent 70%),
      radial-gradient(ellipse 30% 45% at 88% 45%, rgba(236,232,233,0.55), transparent 70%),
      radial-gradient(ellipse 25% 40% at 50% 85%, rgba(236,232,233,0.45), transparent 70%),
      linear-gradient(to bottom, var(--silver-light) 0%, var(--blush-soft) 16%, var(--blush) 42%, var(--blush) 70%, var(--blush-soft) 84%, var(--paper) 100%);
  }
  .banner-mark { position: absolute; left: 161px; top: 31px; width: 214px; height: 159px; background: var(--ink);
    display: flex; align-items: center; justify-content: center; }
  .brand-name { font-family: "Arimo", Arial, sans-serif; font-weight: 400; color: var(--blush); letter-spacing: 0.02em; line-height: 1; }
  .banner-mark .brand-name { font-size: 46px; }
  .tagline { position: absolute; left: 637px; width: 536px; top: 330px; text-align: center; font-size: 19px; letter-spacing: 0.01em; line-height: 1; }

  /* Shared label parts */
  .label { position: absolute; background: var(--blush); overflow: hidden; }
  .label-pattern { position: absolute; inset: 0;
    background:
      radial-gradient(circle at 20% 30%, rgba(236,232,233,0.6), transparent 38%),
      radial-gradient(circle at 80% 55%, rgba(236,232,233,0.55), transparent 40%),
      radial-gradient(circle at 35% 85%, rgba(217,212,214,0.5), transparent 40%),
      radial-gradient(circle at 70% 12%, rgba(217,212,214,0.45), transparent 35%),
      linear-gradient(160deg, var(--blush) 0%, var(--blush-deep) 50%, var(--blush) 100%); }
  .label-panel { position: absolute; background: var(--ink); display: flex; flex-direction: column; align-items: center; justify-content: center; text-align: center; }
  .product-name { font-weight: 700; color: var(--label-text); text-transform: uppercase; line-height: 1.2; }
  .step-number { position: absolute; font-family: "Bodoni Moda", Georgia, serif; color: var(--text); text-align: center; line-height: 1; }
  .step-circle { border: 1px solid #333; border-radius: 50%; display: flex; align-items: center; justify-content: center; }

  /* Bottles */
  .label--bottle { width: 146px; top: 474px; border-radius: 0 0 50% 50% / 0 0 14px 14px; }
  .label--cleanser { left: 152px; height: 321px; }
  .label--toner { left: 372px; height: 296px; }
  .label--bottle .label-panel { left: 5px; top: 7px; width: 136px; height: 101px; padding-top: 4px; }
  .label--bottle .brand-name { font-size: 30px; margin-bottom: 10px; }
  .label--bottle .product-name { font-size: 9px; }
  .label--bottle .step-number { left: 0; width: 100%; top: 144px; font-size: 38px; }

  /* Serum jar */
  .label--serum { left: 617px; top: 625px; width: 209px; height: 112px; }
  .label--serum .label-panel { left: 80px; top: 25px; width: 99px; height: 87px; }
  .label--serum .brand-name { font-size: 26px; margin-bottom: 8px; }
  .label--serum .product-name { font-size: 8px; }
  .label--serum .step-number { left: 21px; top: 50px; width: 34px; height: 38px; font-size: 24px; }

  /* Moisturiser jar */
  .label--moisturiser { left: 925px; top: 667px; width: 179px; height: 66px; }
  .label--moisturiser .label-panel { left: 54px; top: 7px; width: 100px; height: 59px; }
  .label--moisturiser .brand-name { font-size: 18px; margin-bottom: 8px; }
  .label--moisturiser .product-name { font-size: 6px; }
  .label--moisturiser .step-number { left: 16px; top: 20px; width: 26px; height: 29px; font-size: 17px; }
</style>
</head>
<body>
<main class="canvas">
  <section class="brand-banner">
    <div class="banner-pattern" role="img" aria-label="Blush pink and silver geometric lattice pattern fading to white at top and bottom"></div>
    <div class="banner-mark"><span class="brand-name">Lumen</span></div>
  </section>
  <p class="tagline">QUIET HEART - BRIGHT FACE</p>

  <article class="label label--bottle label--cleanser">
    <div class="label-pattern" role="img" aria-label="Blush pink label with silver geometric lattice pattern"></div>
    <div class="label-panel"><span class="brand-name">Lumen</span><span class="product-name">Calm<br>Cleanser</span></div>
    <span class="step-number">1</span>
  </article>

  <article class="label label--bottle label--toner">
    <div class="label-pattern" role="img" aria-label="Blush pink label with silver geometric lattice pattern"></div>
    <div class="label-panel"><span class="brand-name">Lumen</span><span class="product-name">Tranquil<br>Toner</span></div>
    <span class="step-number">2</span>
  </article>

  <article class="label label--serum">
    <div class="label-pattern" role="img" aria-label="Blush pink label with silver geometric lattice pattern"></div>
    <span class="step-number step-circle">3</span>
    <div class="label-panel"><span class="brand-name">Lumen</span><span class="product-name">Anti-Ageing<br>Serum</span></div>
  </article>

  <article class="label label--moisturiser">
    <div class="label-pattern" role="img" aria-label="Blush pink label with silver geometric lattice pattern"></div>
    <span class="step-number step-circle">4</span>
    <div class="label-panel"><span class="brand-name">Lumen</span><span class="product-name">Moisturiser</span></div>
  </article>
</main>
</body>
</html>
```